Business Card Design

We need a business card design for our new expansion based in Bloomfield Hills, Michigan. Our company is Quiet Harbor Institute & Wellness Center. Our Academy teaches individuals of all ages and professions to live from their soul. We teach intuitive development, meditation and mindfulness; shamanic healing. And ourr healing center provides holistic services. We offer certification programs that support the ethical practices of Intuitive professionals. Our team of Intuitive Practitioners includes: doctors, psychologists, chiropractor, soul retrievers, mediums, etc who all balance their knowledge with intuitive wisdom.

We want our symbol to be the Blue Morpho Buttefly and the colors on the card to complement it. We want to communicate inspiration, healing and empowerment. Thank you
Updates

Industry/Entity Type

Business

Contact Information for Business Card

Dana Orwick
Medium. Author. Soul Retriever.
Founder, Quiet Harbor

Quiet Harbor

19 North Cedar Mill Drive Suite 100
Fernwood Heights, MI 48517
248-603-7418

www.danaorwick.example

Requirements
Must have
• blue morpho butterfly

```html
<!DOCTYPE html>
<html lang="en">
<head>
<meta charset="utf-8">
<title>Quiet Harbor – Business Card</title>
<link rel="stylesheet" href="https://fonts.googleapis.com/css2?family=Great+Vibes&family=Roboto+Condensed:wght@400;700&display=swap">
<style>
  :root {
    --brand-blue: #2e66b0;
    --morpho-light: #5fa0e6;
    --morpho-deep: #1f4f9e;
    --card-white: #ffffff;
    --stage: #f1f2f4;
    --ink-white: #ffffff;
  }
  * { box-sizing: border-box; margin: 0; padding: 0; }
  html, body {
    width: 1200px; height: 702px; overflow: hidden;
    background: var(--stage);
  }
  .canvas {
    position: relative; width: 1200px; height: 702px;
    display: flex; align-items: center; justify-content: center; gap: 60px;
  }
  .card {
    position: relative; width: 500px; height: 286px; overflow: hidden;
    box-shadow: 0 6px 18px rgba(0,0,0,0.18);
  }

  /* Front */
  .card--front { background: var(--card-white); }
  .front__butterfly {
    position: absolute; left: 50px; top: 48px; width: 190px; height: 150px;
    border-radius: 45% 45% 40% 40%;
    background: radial-gradient(ellipse at center, var(--morpho-light) 0%, var(--brand-blue) 55%, var(--morpho-deep) 100%);
  }
  .front__name {
    position: absolute; right: 34px; top: 92px;
    font-family: 'Great Vibes', cursive;
    font-size: 46px; color: var(--brand-blue); letter-spacing: 1px;
  }
  .front__band {
    position: absolute; left: 0; right: 0; bottom: 0; height: 52px;
    background: var(--brand-blue);
    display: flex; align-items: center; justify-content: flex-end; padding-right: 34px;
  }
  .front__web {
    font-family: 'Roboto Condensed', sans-serif; font-weight: 700;
    font-size: 15px; letter-spacing: 5px; color: var(--ink-white);
  }

  /* Back */
  .card--back { background: var(--brand-blue); }
  .back__main {
    position: absolute; left: 0; right: 0; top: 0; bottom: 56px;
    display: flex; flex-direction: column; align-items: center; justify-content: center;
    color: var(--ink-white); font-family: 'Roboto Condensed', sans-serif;
    padding-top: 30px;
  }
  .back__name { font-weight: 700; font-size: 27px; letter-spacing: 5px; }
  .back__roles { margin-top: 10px; font-size: 11px; letter-spacing: 1.6px; }
  .back__contact {
    position: absolute; left: 0; right: 0; bottom: 0; height: 56px;
    background: var(--card-white);
    display: flex; flex-direction: column; align-items: center; justify-content: center; gap: 5px;
    font-family: 'Roboto Condensed', sans-serif; font-weight: 700;
    font-size: 9.5px; letter-spacing: 1.4px; color: var(--brand-blue);
  }
  .contact__row { display: flex; align-items: center; gap: 14px; }
  .contact__item { display: flex; align-items: center; gap: 5px; }
  .icon { width: 10px; height: 10px; fill: var(--brand-blue); }
</style>
</head>
<body>
<main class="canvas">
  <section class="card card--front" aria-label="Card front">
    <div class="front__butterfly" role="img" aria-label="Blue morpho butterfly with open wings"></div>
    <p class="front__name">Quiet Harbor</p>
    <div class="front__band"><span class="front__web">www.danaorwick.example</span></div>
  </section>

  <section class="card card--back" aria-label="Card back">
    <div class="back__main">
      <h1 class="back__name">DANA ORWICK</h1>
      <p class="back__roles">founder | medium | author | soul retriever</p>
    </div>
    <div class="back__contact">
      <div class="contact__row">
        <span class="contact__item">
          <svg class="icon" viewBox="0 0 10 10"><path d="M5 0a3.5 3.5 0 0 0-3.5 3.5C1.5 6 5 10 5 10s3.5-4 3.5-6.5A3.5 3.5 0 0 0 5 0zm0 5a1.4 1.4 0 1 1 0-2.8A1.4 1.4 0 0 1 5 5z"/></svg>
          19 North Cedar Mill Drive Suite 100 Fernwood Heights, MI 48517
        </span>
      </div>
      <div class="contact__row">
        <span class="contact__item">
          <svg class="icon" viewBox="0 0 10 10"><path d="M2 0.5l1.8 2-0.9 1.3c0.6 1.3 1.6 2.3 2.9 2.9l1.3-0.9 2 1.8-1.2 1.9C4.5 9.3 0.7 5.5 0.2 1.7z"/></svg>
          (248)-603-7418
        </span>
        <span class="contact__item">
          <svg class="icon" viewBox="0 0 10 10"><path d="M0 2h10v6H0z" /><path d="M0 2l5 3.5L10 2" fill="none" stroke="#fff" stroke-width="1"/></svg>
          QuietHarbor444@example.com
        </span>
      </div>
    </div>
  </section>
</main>
</body>
</html>
```